Business card design for IT consulting company

Looking for a simple, modern, clean business card design.
Open to reworking our existing logo.

Attached is our current business cards which we do not like.
Ideally double sided with something simple on the back.
Rectangle / Horizonal only.
No rounded edges on the card.
White as the dominate color is preferred.

Target Market(s)

clients, legal, oil & gas, medical, professionals

Industry/Entity Type

IT, tech, consulting

Contact Information for Business Card

Name, Title, email, phone, cell, website

Font styles to use
Sans Serif

Requirements
Must have
• Clean design
Should not have
• loud colors or unusual fonts, etc

```html
<!DOCTYPE html>
<html lang="en">
<head>
<meta charset="utf-8">
<title>Arvona Solutions – Business Card</title>
<link rel="stylesheet" href="https://fonts.googleapis.com/css2?family=Fira+Sans:wght@400;500;700;800&display=swap">
<style>
  :root {
    --bg-start: #fdf3c6;
    --bg-pink: #ecc8d3;
    --bg-end: #c3c3d7;
    --card-dark: #19172f;
    --ink: #2a2566;
    --white: #ffffff;
    --accent-yellow: #fccf1d;
  }
  * { margin: 0; padding: 0; box-sizing: border-box; }
  html, body { width: 1200px; height: 1200px; overflow: hidden; }
  body {
    position: relative;
    font-family: "Fira Sans", Arial, sans-serif;
    background: linear-gradient(90deg, var(--bg-start) 0%, var(--bg-pink) 30%, var(--bg-end) 100%);
  }
  .card {
    position: absolute;
    left: 225px;
    width: 749px;
    height: 428px;
  }
  .card-front {
    top: 120px;
    background: var(--card-dark);
    display: flex;
    flex-direction: column;
    align-items: center;
    justify-content: center;
    gap: 10px;
  }
  .brand-mark {
    display: flex;
    align-items: center;
    gap: 16px;
    color: var(--white);
    font-weight: 800;
    line-height: 1;
  }
  .brand-mark .brand-dot {
    width: 26px; height: 26px;
    border-radius: 50%;
    background: var(--accent-yellow);
  }
  .card-front .brand-name { font-size: 112px; letter-spacing: -1px; }
  .card-front .brand-tagline {
    color: var(--white);
    font-weight: 800;
    font-size: 78px;
    line-height: 1;
  }
  .card-back {
    top: 651px;
    background: var(--white);
    border: 1px solid var(--ink);
    color: var(--ink);
  }
  .person-name {
    position: absolute;
    left: 78px; top: 68px;
    font-size: 40px;
    font-weight: 800;
  }
  .person-title {
    position: absolute;
    left: 78px; top: 129px;
    font-size: 27px;
    font-weight: 500;
  }
  .contact-list {
    position: absolute;
    left: 78px; top: 226px;
    list-style: none;
    font-size: 21px;
    font-weight: 500;
  }
  .contact-list li {
    display: flex;
    align-items: center;
    height: 37px;
  }
  .contact-icon {
    width: 24px; height: 24px;
    margin-right: 14px;
    flex: none;
  }
  .contact-icon.blank { visibility: hidden; }
  .card-back .brand-mark {
    position: absolute;
    left: 462px; top: 92px;
    color: var(--ink);
    gap: 10px;
  }
  .card-back .brand-name { font-size: 60px; }
  .card-back .brand-dot { width: 16px; height: 16px; }
</style>
</head>
<body>
  <section class="card card-front">
    <div class="brand-mark">
      <span class="brand-name">Arvona</span>
      <span class="brand-dot"></span>
    </div>
    <div class="brand-tagline">Solutions</div>
  </section>

  <section class="card card-back">
    <h1 class="person-name">Maren Holt</h1>
    <p class="person-title">IT Consultant</p>

    <ul class="contact-list">
      <li>
        <svg class="contact-icon" viewBox="0 0 24 24" aria-hidden="true">
          <rect x="1" y="5" width="22" height="14" fill="none" stroke="currentColor" stroke-width="2"/>
          <path d="M1 5 L12 13 L23 5 M1 19 L9 11 M23 19 L15 11" fill="none" stroke="currentColor" stroke-width="1.8"/>
        </svg>
        maren.holt@arvona.ca
      </li>
      <li>
        <svg class="contact-icon" viewBox="0 0 24 24" aria-hidden="true">
          <path fill="currentColor" d="M6.6 2.5c.6-.4 1.4-.3 1.8.3l2 3c.4.6.3 1.3-.2 1.8l-1.3 1.2c.9 2 2.5 3.8 4.5 5l1.3-1.2c.5-.5 1.2-.5 1.8-.1l3 2.1c.6.4.8 1.3.3 1.9l-1.5 1.9c-.8 1-2.1 1.3-3.2.8C9.6 17.3 5.8 13 3.9 7.6c-.4-1.1 0-2.3.9-3z"/>
        </svg>
        (555) 014-2290
      </li>
      <li>
        <span class="contact-icon blank"></span>
        (555) 014-7731
      </li>
      <li>
        <svg class="contact-icon" viewBox="0 0 24 24" aria-hidden="true">
          <g fill="none" stroke="currentColor" stroke-width="1.5">
            <circle cx="12" cy="12" r="10.5"/>
            <ellipse cx="12" cy="12" rx="4.5" ry="10.5"/>
            <path d="M12 1.5v21M1.5 12h21M3 7h18M3 17h18"/>
          </g>
        </svg>
        www.arvona.ca
      </li>
    </ul>

    <div class="brand-mark">
      <span class="brand-name">Arvona</span>
      <span class="brand-dot"></span>
    </div>
  </section>
</body>
</html>
```